Label design for Cargo Pants.

We need modern packaging design for men's cargo pant for a brand name Talvo. All kinds of packaging designs are welcome.

The pant is folded and packaged in a poly bag. We require a label design for the brand name Talvo. The main label will be attached by a string on the belt loop. the size of that label will 25cm in length and 10cm wide. This is the first label the customer see's when he picks up the garment. Therefore, we require an eye catching design for that. If required it could have certain information about the chino pant on the main label such as Comfort fit, Wrinkle-resistant, machine washable, luxury fabric. But, if you feel that adding the above information spoils the design of the label then it is not a must to include the above information. On the back of the label we like to include the information that this pant was manufactured in an Vesk Summit certified green plant and hence the damage to the environment because of the plant is nill.

The second label is attached on to the waist band and the purpose of that label is to include the size of the pant such 32x32. The size of that label is 8cm in length and 4cm in width. There is no design on the back on this label it has to be blank.

Sample, is provided for what we use for our chino pant.

```html
<!DOCTYPE html>
<html lang="en">
<head>
<meta charset="utf-8">
<title>Talvo Chinos – Hang Tag Options</title>
<link href="https://fonts.googleapis.com/css2?family=Oswald:wght@500;600&family=Montserrat:wght@600&display=swap" rel="stylesheet">
<style>
  :root {
    --canvas: #ececec;
    --ink-dark: #2a221e;
    --ink-light: #ffffff;
    --band: #2b2320;
    --pill-dark: #2a2320;
    --stone-1: #cfc5b8;
    --stone-2: #a99b8b;
    --slate-1: #6a615a;
    --slate-2: #3e3733;
    --bark-1: #6b4528;
    --bark-2: #3a2414;
    --caption: #222222;
  }
  * { box-sizing: border-box; margin: 0; padding: 0; }
  html, body { width: 1200px; height: 857px; overflow: hidden; }
  body {
    position: relative;
    background: radial-gradient(ellipse at center, #fafafa 0%, var(--canvas) 75%, #dedede 100%);
    font-family: "Oswald", "Arial Narrow", sans-serif;
  }
  .tag {
    position: absolute;
    top: 37px;
    width: 292px;
    height: 731px;
    overflow: hidden;
    box-shadow: 0 3px 10px rgba(0,0,0,0.25);
    text-align: center;
  }
  .tag--stone { left: 114px; background: radial-gradient(ellipse at 50% 55%, var(--stone-1) 0%, var(--stone-2) 100%); color: var(--ink-dark); }
  .tag--slate { left: 455px; background: radial-gradient(ellipse at 50% 55%, var(--slate-1) 0%, var(--slate-2) 100%); color: var(--ink-light); }
  .tag--bark  { left: 792px; background: radial-gradient(ellipse at 50% 60%, var(--bark-1) 0%, var(--bark-2) 85%, #1e140c 100%); color: var(--ink-light); }

  .tag__artwork {
    position: absolute;
    left: 0; top: 25px;
    width: 290px; height: 240px;
  }
  .tag--stone .tag__artwork { background: radial-gradient(ellipse 70% 55% at 40% 62%, rgba(30,24,20,0.85) 0%, rgba(30,24,20,0.5) 50%, rgba(30,24,20,0) 100%); }
  .tag--slate .tag__artwork { background: radial-gradient(ellipse 70% 55% at 40% 62%, rgba(30,22,18,0.8) 0%, rgba(30,22,18,0.45) 50%, rgba(30,22,18,0) 100%); }

  .tag__brand {
    position: absolute;
    left: 0; right: 0;
    top: 258px;
    height: 110px;
    font-family: "Oswald", "Arial Narrow", sans-serif;
    font-weight: 600;
    font-size: 92px;
    line-height: 110px;
    letter-spacing: 4px;
  }
  .tag--bark .tag__brand { top: 160px; font-size: 86px; }

  .tag__features {
    position: absolute;
    left: 0; right: 0;
    top: 384px;
    list-style: none;
    font-weight: 500;
    font-size: 26px;
    line-height: 31.5px;
    text-transform: uppercase;
  }
  .tag--bark .tag__features { top: 289px; font-size: 27px; line-height: 53px; }

  .tag__product {
    position: absolute;
    left: 9px; right: 9px;
    top: 533px;
    height: 60px;
    border-radius: 10px;
    background: var(--pill-dark);
    font-weight: 500;
    font-size: 42px;
    line-height: 60px;
    text-transform: uppercase;
  }
  .tag--stone .tag__product { color: var(--stone-1); }
  .tag--slate .tag__product { color: var(--ink-light); }
  .tag--bark .tag__product { top: 509px; height: 58px; line-height: 58px; background: #2a1e18; }

  .tag__note {
    position: absolute;
    left: 18px; right: 18px;
    top: 611px;
    font-weight: 500;
    font-size: 11.5px;
    line-height: 14px;
  }
  .tag--bark .tag__note { top: 603px; }

  .tag__slogan {
    position: absolute;
    left: 0; right: 0; bottom: 0;
    height: 58px;
    background: var(--band);
    color: var(--ink-light);
    font-weight: 500;
    font-size: 16px;
    line-height: 58px;
    text-transform: uppercase;
  }
  .tag--bark .tag__slogan { background: #241a14; }

  .option-caption {
    position: absolute;
    top: 789px;
    width: 292px;
    text-align: center;
    font-family: "Montserrat", Arial, sans-serif;
    font-weight: 600;
    font-size: 24px;
    letter-spacing: 1px;
    color: var(--caption);
  }
</style>
</head>
<body>
  <section class="tag tag--stone">
    <div class="tag__artwork" role="img" aria-label="Dark silhouette of a moose head with antlers"></div>
    <h1 class="tag__brand">TALVO</h1>
    <ul class="tag__features">
      <li>Comfort Fit</li><li>Wrinkle Resistant</li><li>Machine Washable</li><li>Luxury Fabrix</li>
    </ul>
    <p class="tag__product">Men's Chinos</p>
    <p class="tag__note">This Talvo Chino was proudly produced in a Vesk Summit certified green plan with no negative environmental impact</p>
    <p class="tag__slogan">Help the environment, buy a Talvo!</p>
  </section>
  <p class="option-caption" style="left:114px">OPTION 1</p>

  <section class="tag tag--slate">
    <div class="tag__artwork" role="img" aria-label="Dark silhouette of a moose head with antlers"></div>
    <h1 class="tag__brand">TALVO</h1>
    <ul class="tag__features">
      <li>Comfort Fit</li><li>Wrinkle Resistant</li><li>Machine Washable</li><li>Luxury Fabrix</li>
    </ul>
    <p class="tag__product">Men's Chinos</p>
    <p class="tag__note">This Talvo Chino was proudly produced in a Vesk Summit certified green plan with no negative environmental impact</p>
    <p class="tag__slogan">Help the environment, buy a Talvo!</p>
  </section>
  <p class="option-caption" style="left:455px">OPTION 2</p>

  <section class="tag tag--bark">
    <h1 class="tag__brand">TALVO</h1>
    <ul class="tag__features">
      <li>Comfort Fit</li><li>Wrinkle Resistant</li><li>Machine Washable</li><li>Luxury Fabrix</li>
    </ul>
    <p class="tag__product">Men's Chinos</p>
    <p class="tag__note">This Talvo Chino was proudly produced in a Vesk Summit certified green plan with no negative environmental impact</p>
    <p class="tag__slogan">Help the environment, buy a Talvo!</p>
  </section>
  <p class="option-caption" style="left:792px">OPTION 3</p>
</body>
</html>
```